KTR Engineering Pty Ltd

I have already had Corvale welding and fabrication cards made , my business has changed too KTR engineering Pty Ltd so I need my logo changed on the cards
one side have my logo then the other side have what we do.
front side logo and details
owner /operator : Lachlan Meravic
email: ktr.works@ironvalemail.com
number: 0491537204
ABN: 47 261 538 902
ACN: 718 352 946
on back have in dot points what we do:
* structural steel erection
* precast panels
* site welding
*steel alteration & repair
* rigging & dogging
*labour hire
all details in breif

```html
<!DOCTYPE html>
<html lang="en">
<head>
<meta charset="UTF-8">
<title>KTR Engineering Pty Ltd – Business Card</title>
<link href="https://fonts.googleapis.com/css2?family=Open+Sans:wght@400;600;800&display=swap" rel="stylesheet">
<style>
  :root {
    --stage: #232323;
    --navy: #1b2431;
    --navy-text: #1f2a3a;
    --brick: #9c3f37;
    --white: #ffffff;
    --ink: #1a1a1a;
    --muted-steel: #7d8796;
  }
  * { box-sizing: border-box; margin: 0; padding: 0; }
  html, body { width: 1200px; height: 780px; overflow: hidden; }
  body {
    background: var(--stage);
    font-family: "Open Sans", Arial, sans-serif;
    display: flex;
    align-items: center;
    justify-content: center;
    gap: 70px;
  }
  .card {
    width: 360px;
    height: 590px;
    border-radius: 26px;
    position: relative;
    overflow: hidden;
  }

  /* Logo side */
  .card--brand {
    background: var(--navy);
    display: flex;
    align-items: center;
    justify-content: center;
  }
  .brand-mark {
    display: flex;
    align-items: center;
    gap: 14px;
  }
  .brand-mark__dot {
    width: 22px; height: 22px; border-radius: 50%;
    background: var(--muted-steel);
    flex: none;
  }
  .brand-mark__name {
    color: var(--muted-steel);
    font-weight: 800;
    font-size: 26px;
    line-height: 1.15;
    text-transform: uppercase;
    letter-spacing: 0.5px;
  }

  /* Details side */
  .card--details {
    background: var(--white);
    display: flex;
    flex-direction: column;
    align-items: center;
    text-align: center;
    padding-top: 50px;
  }
  .company-name {
    color: var(--navy-text);
    font-weight: 800;
    font-size: 25px;
    line-height: 1.15;
    text-transform: uppercase;
    display: flex;
    align-items: center;
    gap: 10px;
  }
  .company-name__dot {
    width: 16px; height: 16px; border-radius: 50%;
    background: var(--brick);
    flex: none;
  }
  .person { margin-top: 68px; }
  .person__name {
    font-weight: 800;
    font-size: 29px;
    line-height: 1.1;
  }
  .person__first { color: var(--brick); }
  .person__last { color: var(--navy-text); }
  .person__role {
    font-size: 17px;
    color: var(--ink);
    margin-top: 2px;
  }
  .contact-icons {
    display: flex; gap: 8px; justify-content: center;
    margin-top: 10px;
  }
  .contact-icons svg { width: 24px; height: 24px; }
  .contact {
    font-size: 17px;
    color: var(--ink);
    line-height: 1.35;
    margin-top: 4px;
  }
  .services-label {
    display: inline-block;
    margin-top: 12px;
    background: var(--brick);
    color: var(--white);
    font-size: 13px;
    font-weight: 600;
    padding: 3px 22px;
    border-radius: 50%;
  }
  .services {
    list-style: none;
    font-size: 15.5px;
    line-height: 1.32;
    color: var(--ink);
    margin-top: 6px;
  }
  .registration {
    position: absolute;
    left: 0; right: 0; bottom: 18px;
    background: var(--brick);
    color: var(--white);
    font-size: 14.5px;
    font-weight: 600;
    padding: 8px 0;
    text-align: center;
  }
</style>
</head>
<body>
  <section class="card card--brand" aria-label="Card logo side">
    <div class="brand-mark">
      <span class="brand-mark__dot"></span>
      <span class="brand-mark__name">KTR Engineering<br>Pty Ltd</span>
    </div>
  </section>

  <section class="card card--details" aria-label="Card details side">
    <div class="company-name">
      <span class="company-name__dot"></span>
      <span>KTR Engineering<br>Pty Ltd</span>
    </div>

    <div class="person">
      <h1 class="person__name"><span class="person__first">Lachlan</span> <span class="person__last">Meravic</span></h1>
      <p class="person__role">owner /operator</p>
    </div>

    <div class="contact-icons">
      <svg viewBox="0 0 24 24" aria-label="Phone"><circle cx="12" cy="12" r="12" fill="#9c3f37"/><path d="M8.2 6.5l2 2.3-1.1 1.4c.8 1.7 2 2.9 3.7 3.7l1.4-1.1 2.3 2-1 1.7c-4.2-.3-8-4.1-8.3-8.3z" fill="#fff"/></svg>
      <svg viewBox="0 0 24 24" aria-label="Email"><circle cx="12" cy="12" r="12" fill="#9c3f37"/><rect x="6" y="8" width="12" height="8.5" rx="1" fill="none" stroke="#fff" stroke-width="1.4"/><path d="M6.5 8.7L12 13l5.5-4.3" fill="none" stroke="#fff" stroke-width="1.4"/></svg>
    </div>
    <p class="contact">0491537204<br>ktr.works@ironvalemail.com</p>

    <span class="services-label">WHAT WE DO</span>
    <ul class="services">
      <li>Site welding</li>
      <li>Labour hire</li>
      <li>Precast panels</li>
      <li>Rigging &amp; dogging</li>
      <li>Structural steel erection</li>
      <li>Steel alteration &amp; repair</li>
    </ul>

    <p class="registration">ABN: 47 261 538 902/ACN: 718 352 946</p>
  </section>
</body>
</html>
```